Retail Jewelry Business Card Design Project

We are in need of a new business card design for a retail jewelry store. This store is in the business of fine jewelry including but not specific to bridal jewelry, diamonds, designer jewelry and watches.

This store has been in business for 20 years but continues to strive for a modern professional appeal. The main colors use for this business are a royal blue, white and silver.

Target Market(s)

Target market is ages 18-50

Industry/Entity Type

Jewelry

Requirements
Must have
• Sales Person Name
Sales Person Email Address

Store Address
Store Phone
Website

Standard business card size. No odd shapes or sizes.
Nice to have
• Overall modern feel for card.

We have thought that a design with a nice feature of the logo on the back of the card would be nice but open to ideas.
Should not have
• No specific images of jewelry should be used.

```html
<!DOCTYPE html>
<html lang="en">
<head>
<meta charset="utf-8">
<title>Marlow Crane Fine Jewelry – Business Card</title>
<link href="https://fonts.googleapis.com/css2?family=Courier+Prime:wght@400;700&display=swap" rel="stylesheet">
<style>
  :root {
    --stage-blue: #0a78c8;
    --card-black: #262626;
    --silver: #b9bcc0;
    --rule-silver: #9a9da1;
    --ink-white: #ffffff;
    --icon-white: #f2f2f2;
  }
  html, body {
    margin: 0;
    padding: 0;
    width: 1200px;
    height: 1003px;
    overflow: hidden;
    background: var(--stage-blue);
    font-family: "Courier Prime", "Courier New", monospace;
  }
  .stage {
    position: relative;
    width: 1200px;
    height: 1003px;
  }
  .card {
    position: absolute;
    left: 150px;
    top: 227px;
    width: 900px;
    height: 549px;
    box-shadow: 0 6px 18px rgba(0, 0, 0, 0.35);
    overflow: hidden;
  }
  .card-pattern {
    position: absolute;
    inset: 0;
    background: var(--card-black);
  }
  .brand-name {
    position: absolute;
    right: 80px;
    top: 84px;
    margin: 0;
    color: var(--silver);
    font-weight: 400;
    font-size: 36px;
    letter-spacing: 1px;
    white-space: nowrap;
  }
  .brand-rule {
    position: absolute;
    left: 0;
    top: 138px;
    width: 830px;
    height: 3px;
    background: var(--rule-silver);
  }
  .person-name {
    position: absolute;
    left: 54px;
    top: 182px;
    margin: 0;
    color: var(--ink-white);
    font-weight: 700;
    font-size: 32px;
    line-height: 46px;
  }
  .person-phone {
    position: absolute;
    left: 54px;
    top: 318px;
    margin: 0;
    color: var(--ink-white);
    font-weight: 400;
    font-size: 34px;
  }
  .store-address {
    position: absolute;
    left: 389px;
    top: 238px;
    margin: 0;
    font-style: normal;
    color: var(--ink-white);
    font-size: 25px;
    line-height: 35px;
  }
  .contact-list {
    position: absolute;
    left: 402px;
    top: 380px;
    margin: 0;
    padding: 0;
    list-style: none;
    color: var(--ink-white);
    font-size: 24px;
    line-height: 34px;
  }
  .contact-list li {
    display: flex;
    align-items: center;
    gap: 14px;
  }
  .contact-list svg {
    width: 20px;
    height: 20px;
    flex: none;
  }
  .contact-web {
    font-weight: 700;
  }
</style>
</head>
<body>
<main class="stage">
  <article class="card">
    <div class="card-pattern" role="img" aria-label="Dark charcoal card background with a subtle repeating fleur-de-lis pattern"></div>

    <h1 class="brand-name">Marlow Crane Fine Jewelry</h1>
    <div class="brand-rule"></div>

    <h2 class="person-name">Evan Marlow<br>Hartley</h2>
    <p class="person-phone">189 555 0142</p>

    <address class="store-address">
      Marlow Crane Fine<br>
      2280 Linden Avenue<br>
      Bayport, FL 32900
    </address>

    <ul class="contact-list">
      <li>
        <svg viewBox="0 0 20 20" aria-hidden="true"><path fill="var(--icon-white)" d="M3 7c0-2 3-3 7-3s7 1 7 3v1h-4V6.5H7V8H3zM5 9h10l1 8H4z"/></svg>
        <span>+(0) 55 01 42 235</span>
      </li>
      <li>
        <svg viewBox="0 0 20 20" aria-hidden="true"><rect x="5" y="2" width="10" height="6" fill="var(--icon-white)"/><rect x="2" y="8" width="16" height="10" rx="1" fill="var(--icon-white)"/><rect x="5" y="12" width="10" height="2" fill="var(--card-black)"/></svg>
        <span>+(0) 55 01 42 236</span>
      </li>
      <li>
        <svg viewBox="0 0 20 20" aria-hidden="true"><rect x="2" y="4" width="16" height="12" fill="var(--icon-white)"/><path d="M2 4l8 7 8-7" fill="none" stroke="var(--card-black)" stroke-width="1.5"/></svg>
        <span>evan@marlowcranejewelry.com</span>
      </li>
      <li>
        <svg viewBox="0 0 20 20" aria-hidden="true"><circle cx="10" cy="10" r="8" fill="var(--icon-white)"/><path d="M2 10h16M10 2c-3 3-3 13 0 16M10 2c3 3 3 13 0 16" fill="none" stroke="var(--card-black)" stroke-width="1.2"/></svg>
        <span class="contact-web">www.marlowcranejewelry.com</span>
      </li>
    </ul>
  </article>
</main>
</body>
</html>
```